Flyer Designer for a Widow and Door Company - loooking for fresh design

We are looking for a flyer designed to advertise our business - we supply and install windows and doors - we are looking for a fresh looking flyer to distribute to drum up business - more information can be found at our website www.brightpanehouse.co.uk - We want a different approach than we currently have - making it vibrant and fresh - you can see the services on the website but its more the graphical design that we are looking for rather than content as the content from the website can be used for each service etc.

Target Market(s)

the general public

Colors

Designer to choose colors to be used in the design.

Requirements
Must have
• vibrant design and images

```html
<!DOCTYPE html>
<html lang="en">
<head>
<meta charset="utf-8">
<title>Bright Pane House Ltd – Flyer</title>
<link href="https://fonts.googleapis.com/css2?family=Roboto:ital,wght@0,400;0,500;0,700;1,700&display=swap" rel="stylesheet">
<style>
  :root {
    --page-bg: #d9d9d9;
    --brand-blue: #1a6fc4;
    --brand-blue-deep: #0d3f7a;
    --panel-top: #1c6cc2;
    --panel-bottom: #0f3d73;
    --accent-light: #8cc4ff;
    --hex-stroke: #2a6cc0;
    --text-dark: #1f2a36;
    --grey-band: #8f9296;
    --button-grey: #6d7075;
    --white: #ffffff;
    --logo-grey: #5b5f66;
  }
  * { margin: 0; padding: 0; box-sizing: border-box; }
  html, body { width: 1200px; height: 1000px; overflow: hidden; background: var(--page-bg); }
  body { position: relative; font-family: "Roboto", Arial, sans-serif; }

  .flyer {
    position: absolute; left: 259px; top: 66px; width: 682px; height: 882px;
    overflow: hidden;
    background: linear-gradient(180deg, #f4f6f8 0%, #f1ece0 40%, #eadfc3 70%, #d8d2c6 88%, #bfbab4 100%);
  }
  .room-photo {
    position: absolute; inset: 0;
    background:
      radial-gradient(ellipse at 40% 20%, rgba(255,255,255,.9), rgba(255,255,255,0) 60%),
      linear-gradient(180deg, rgba(220,230,238,.5) 0%, rgba(240,226,190,.4) 60%, rgba(170,165,160,.45) 100%);
  }
  .artwork { position: absolute; inset: 0; width: 682px; height: 882px; }

  .headline {
    position: absolute; left: 40px; top: 40px; width: 380px;
    color: var(--brand-blue); font-weight: 700; font-size: 27.5px; line-height: 36px;
  }
  .intro {
    position: absolute; left: 40px; top: 116px; width: 373px;
    color: var(--text-dark); font-size: 9.6px; line-height: 13px; text-align: justify;
  }

  .services {
    position: absolute; left: 319px; top: 264px; width: 340px; height: 418px;
    border-radius: 14px; padding: 14px 18px 0 18px;
    background: linear-gradient(180deg, var(--panel-top) 0%, #1655a0 45%, var(--panel-bottom) 100%);
    color: var(--white);
  }
  .service-group { margin-bottom: 13px; }
  .service-title { font-size: 13.5px; font-weight: 700; letter-spacing: .1px; }
  .service-title span { color: var(--accent-light); font-weight: 500; }
  .service-lead { font-size: 9.2px; line-height: 11.5px; margin-top: 3px; color: #e6f0fb; }
  .service-list {
    list-style: none; display: grid; grid-template-columns: 82px 109px auto;
    column-gap: 0; row-gap: 4px; margin-top: 8px; padding-left: 13px;
    font-size: 10.8px; font-weight: 700; line-height: 11px;
  }
  .service-list li { position: relative; padding-left: 10px; }
  .service-list li::before {
    content: ""; position: absolute; left: 0; top: 2px; width: 5px; height: 5px;
    background: var(--accent-light);
  }

  .quote-button {
    position: absolute; left: 345px; top: 658px; width: 286px; height: 38px;
    background: var(--button-grey); color: var(--white);
    font-size: 19.5px; font-weight: 700; font-style: italic; letter-spacing: .3px;
    display: flex; align-items: center; justify-content: center;
    box-shadow: 0 3px 6px rgba(0,0,0,.35);
  }

  .brand {
    position: absolute; left: 338px; top: 748px; width: 300px;
    display: flex; align-items: center; gap: 12px;
  }
  .brand-mark { width: 46px; height: 46px; background: var(--brand-blue); flex: none; }
  .brand-name { color: var(--brand-blue); font-size: 27px; font-weight: 700; line-height: 29px; }

  .footer { position: absolute; left: 0; top: 831px; width: 682px; height: 51px; }
  .footer-address {
    position: absolute; left: 29px; top: 12px; width: 300px;
    color: var(--white); font-size: 9.6px; font-weight: 700; line-height: 13px;
  }
  .footer-contacts {
    position: absolute; left: 362px; top: 13px;
    color: var(--white); font-size: 9.6px; line-height: 14px;
    display: grid; grid-template-columns: 36px 90px auto; column-gap: 0;
  }
  .footer-contacts .label { font-weight: 700; }
  .footer-contacts svg { width: 8px; height: 8px; vertical-align: -1px; margin-right: 3px; }
</style>
</head>
<body>
  <main class="flyer">
    <div class="room-photo" role="img" aria-label="Bright conservatory interior with white windows and a chequered tiled floor"></div>

    <svg class="artwork" viewBox="0 0 682 882" aria-hidden="false">
      <!-- footer bands -->
      <polygon points="0,831 682,831 682,882 0,882" fill="var(--grey-band)"/>
      <polygon points="0,831 330,831 362,882 0,882" fill="var(--brand-blue)"/>

      <!-- feature door -->
      <polygon role="img" aria-label="Black composite front door set in a stone archway"
        points="438,124 494,18 626,18 682,124 626,230 494,230"
        fill="#a89576" stroke="var(--white)" stroke-width="2"/>

      <!-- product gallery -->
      <g stroke="var(--hex-stroke)" stroke-width="1.5">
        <polygon role="img" aria-label="White French doors in a brick wall" points="154,346 189,279 276,279 311,346 276,414 189,414" fill="#7a6a5a"/>
        <polygon role="img" aria-label="Open white uPVC French doors" points="27,420 61,352 147,352 181,420 147,487 61,487" fill="#b8b2a6"/>
        <polygon role="img" aria-label="Red composite door with leaded glass panels" points="154,491 189,424 276,424 311,491 276,559 189,559" fill="#a8202a"/>
        <polygon role="img" aria-label="Pale blue composite door beside a garden" points="27,563 61,496 147,496 181,563 147,631 61,631" fill="#8aa0b3"/>
        <polygon role="img" aria-label="White casement window in a hallway" points="154,639 189,571 276,571 311,639 276,707 189,707" fill="#cfc4b0"/>
        <polygon role="img" aria-label="White sash window seen from inside" points="27,711 61,644 147,644 181,711 147,779 61,779" fill="#d9d4cb"/>
      </g>
    </svg>

    <h1 class="headline">Installers and Suppliers of Bespoke Windows and Doors</h1>
    <p class="intro">The Bright Pane House team have many years’ experience supplying and fitting the highest quality windows and doors throughout Westshire. Our experienced, friendly team are able to offer a personal touch to your project ensuring you are fully informed at all times and completely happy with the product choices you have made. All of our surveying is kept in house by our installation team which has been selected to carry out your installation. This ensures that when our team arrive at your home to install your windows and doors, you can be confident that your installation will be a smooth process with no surprises</p>

    <section class="services">
      <div class="service-group">
        <h2 class="service-title">OUR <span>WINDOWS</span></h2>
        <p class="service-lead">At Bright Pane House we can supply and fit a huge range of window designs to suit your individual needs.</p>
        <ul class="service-list">
          <li>Casement</li><li>Tilt-and-Turn</li><li>Vertical slider / sash windows</li>
          <li>Bow or bay window</li><li>French windows</li>
        </ul>
      </div>
      <div class="service-group">
        <h2 class="service-title">OUR <span>DOORS</span></h2>
        <p class="service-lead">At Bright Pane House we can supply and fit a huge range of window designs to suit your individual needs.</p>
        <ul class="service-list">
          <li>Composite Doors</li><li>Bifolding Doors</li><li>uPVC Doors</li>
          <li>Patio Doors</li><li>French Doors</li><li>Stable Doors</li>
        </ul>
      </div>
      <div class="service-group">
        <h2 class="service-title">REP<span>AIRS</span></h2>
        <ul class="service-list">
          <li>Window Repairs</li><li>Door Repairs</li><li>Glass Units</li>
          <li>Hardware</li><li>Adjustments</li><li>Cat Flap Services</li>
        </ul>
      </div>
      <div class="service-group">
        <h2 class="service-title">LANDLORD <span>SERVICES</span></h2>
        <ul class="service-list">
          <li>Repairs</li><li>Replacments</li><li>Adjustments</li>
          <li>Surveys</li>
        </ul>
      </div>
    </section>

    <div class="quote-button">REQUEST A FREE QUOTE</div>

    <div class="brand">
      <span class="brand-mark"></span>
      <span class="brand-name">BRIGHT PANE HOUSE LTD</span>
    </div>

    <footer class="footer">
      <p class="footer-address">Bright Pane House Ltd Millbrook House Canal Road Oakridge Westshire OK4 7TR</p>
      <div class="footer-contacts">
        <span class="label">Sales:</span>
        <span><svg viewBox="0 0 10 10"><path d="M2 1 L4 1 L5 3 L4 4 Q5 6 6 6 L7 5 L9 6 L9 8 Q8 9 7 9 Q1 8 1 2 Q1 1 2 1Z" fill="#fff"/></svg>01632 960 260</span>
        <span><svg viewBox="0 0 10 10"><rect x="1" y="2" width="8" height="6" fill="none" stroke="#fff"/><path d="M1 2 L5 5 L9 2" fill="none" stroke="#fff"/></svg>sales@brightpanehouse.co.uk</span>
        <span class="label">Office:</span>
        <span><svg viewBox="0 0 10 10"><path d="M2 1 L4 1 L5 3 L4 4 Q5 6 6 6 L7 5 L9 6 L9 8 Q8 9 7 9 Q1 8 1 2 Q1 1 2 1Z" fill="#fff"/></svg>01632 960 261</span>
        <span><svg viewBox="0 0 10 10"><rect x="1" y="2" width="8" height="6" fill="none" stroke="#fff"/><path d="M1 2 L5 5 L9 2" fill="none" stroke="#fff"/></svg>enquiries@brightpanehouse.co.uk</span>
      </div>
    </footer>
  </main>
</body>
</html>
```